Business Card Design Project

I am community manager and social media strategist. I need a double sided business card with company logo and name. Looking for something professional, elegant but also a little bit original.

• - The logo and the colours are the company colours and a required to stay.
- The size should be: 84 x 55 mm (or 3.30 x 2.16)
- The file size should be: 1039 x 697 pixels (300 dpi)
- I'd like rounded corners. :)

Use the following contact information for the card:

Léonie Vardin
Stratégie médias sociaux / community management / édition de sites sociaux
mob. : 0687529103
leonie.vardin@postelune.fr
Twitter. : @lvardin
Skype : vardin.leonie

```html
<!DOCTYPE html>
<html lang="fr">
<head>
<meta charset="utf-8">
<title>Norvelle – carte de visite</title>
<link rel="stylesheet" href="https://fonts.googleapis.com/css2?family=Source+Sans+3:wght@300;400;600;700&display=swap">
<style>
  :root {
    --stage-top: #e6e6e6;
    --stage-bottom: #a9a9a9;
    --label-grey: #6f6f6f;
    --card-white: #ffffff;
    --brand-blue: #1d6a98;
    --deep-blue: #134b6c;
    --band-light: #1f5d80;
    --band-dark: #154563;
    --text-white: #ffffff;
  }
  * { margin: 0; padding: 0; box-sizing: border-box; }
  html, body { width: 1200px; height: 547px; overflow: hidden; }
  body {
    position: relative;
    font-family: "Source Sans 3", sans-serif;
    background: linear-gradient(180deg, var(--stage-top) 0%, var(--stage-bottom) 100%);
  }
  .side-label {
    position: absolute;
    top: 70px;
    width: 300px;
    text-align: center;
    font-size: 46px;
    font-weight: 300;
    color: var(--label-grey);
    line-height: 1;
  }
  .side-label--front { left: 188px; }
  .side-label--back { left: 715px; }

  .card {
    position: absolute;
    top: 140px;
    width: 496px;
    height: 323px;
    border-radius: 34px;
    overflow: hidden;
  }
  .card--front { left: 90px; background: var(--card-white); }
  .card--back {
    left: 615px;
    background: radial-gradient(ellipse at 40% 35%, #1f5f82 0%, #174e6e 55%, #103f5a 100%);
  }

  .brand {
    position: absolute;
    display: flex;
    align-items: center;
    gap: 10px;
    font-weight: 600;
    letter-spacing: 1px;
    line-height: 1;
  }
  .brand__dot { border-radius: 50%; flex: none; }
  .brand--front { right: 36px; top: 74px; color: var(--brand-blue); font-size: 25px; }
  .brand--front .brand__dot { width: 22px; height: 22px; background: var(--brand-blue); }
  .brand--back {
    left: 0; right: 0; top: 140px;
    justify-content: center;
    color: var(--text-white); font-size: 33px;
  }
  .brand--back .brand__dot { width: 34px; height: 34px; background: var(--text-white); }

  .contact-band {
    position: absolute;
    left: 0; top: 123px;
    width: 100%; height: 136px;
    background: linear-gradient(100deg, var(--band-light) 0%, var(--band-dark) 100%);
    color: var(--text-white);
    padding: 9px 0 0 51px;
  }
  .contact-band__name { font-size: 22px; font-weight: 700; line-height: 25px; }
  .contact-band__role { font-size: 15px; font-weight: 600; line-height: 19px; margin-bottom: 6px; }
  .contact-list { list-style: none; font-size: 13px; line-height: 16.5px; font-weight: 400; }
  .contact-list strong { font-weight: 600; }

  .services {
    position: absolute;
    left: 50px; top: 273px;
    font-size: 12.5px;
    color: var(--deep-blue);
    white-space: nowrap;
  }
</style>
</head>
<body>
  <div class="side-label side-label--front">Front</div>
  <div class="side-label side-label--back">Back</div>

  <section class="card card--front">
    <div class="brand brand--front"><span class="brand__dot"></span>NORVELLE</div>
    <div class="contact-band" role="img" aria-label="Bande bleue texturée portant les coordonnées">
      <p class="contact-band__name">Léonie Vardin</p>
      <p class="contact-band__role">community manager and social media strategist</p>
      <ul class="contact-list">
        <li>Mob: <strong>0687529103</strong></li>
        <li>E-mail: <strong>leonie.vardin@postelune.fr</strong></li>
        <li>Twitter: <strong>@lvardin</strong></li>
        <li>Skype: <strong>vardin.leonie</strong></li>
      </ul>
    </div>
    <p class="services">Stratégie médias sociaux | Community management | Édition de sites sociaux</p>
  </section>

  <section class="card card--back" role="img" aria-label="Fond bleu profond texturé avec le nom de la société">
    <div class="brand brand--back"><span class="brand__dot"></span>NORVELLE</div>
  </section>
</body>
</html>
```